Clearpath Waste Co Business Card

Hey,
I need a double sided business card designed for a rubbish removal business based in Australia. Logo is already chosen, similar colours preferred for both sides of the business card.

Details to include:

Front:

Clearpath Waste Co
Darren Holloway
Managing Director
Mobile: 0491 570 156
Email: darren@clearpathwaste.com.au
Website: clearpathwaste.com.au

Rear:

How did we do?
clearpathwaste.com.au/review

```html
<!DOCTYPE html>
<html lang="en">
<head>
<meta charset="utf-8">
<title>Clearpath Waste Co – Business Card</title>
<link href="https://fonts.googleapis.com/css2?family=Poppins:wght@400;500;600;700&family=Roboto+Condensed:wght@800&display=swap" rel="stylesheet">
<style>
  :root {
    --page: #e6e8e7;
    --green: #1db544;
    --green-dark: #14a23a;
    --green-light: #9fdf3c;
    --ink: #111;
    --muted: #555;
    --white: #fff;
  }
  * { box-sizing: border-box; margin: 0; padding: 0; }
  html, body { width: 1200px; height: 900px; overflow: hidden; }
  body {
    background: var(--page);
    font-family: "Poppins", sans-serif;
    position: relative;
  }
  .card {
    position: absolute;
    left: 267px;
    width: 665px;
    height: 380px;
    overflow: hidden;
    box-shadow: 0 6px 18px rgba(0,0,0,.15);
  }

  /* Front */
  .card--front { top: 45px; background: var(--white); }
  .side-bar {
    position: absolute;
    left: 0;
    width: 26px;
    background: linear-gradient(180deg, var(--green-light), var(--green));
  }
  .side-bar--top { top: 0; height: 150px; }
  .side-bar--bottom { bottom: 0; height: 95px; background: linear-gradient(0deg, var(--green-light), var(--green)); }
  .identity { position: absolute; left: 48px; top: 38px; }
  .identity__name {
    font-family: "Roboto Condensed", sans-serif;
    font-weight: 800;
    font-size: 36px;
    letter-spacing: .5px;
    color: var(--ink);
    line-height: 1;
    text-transform: uppercase;
  }
  .identity__role { font-size: 16px; color: var(--muted); margin-top: 4px; }
  .contacts { position: absolute; left: 0; top: 168px; list-style: none; }
  .contacts__item {
    display: flex;
    align-items: center;
    gap: 14px;
    height: 32px;
    font-size: 17px;
    color: var(--ink);
  }
  .contacts__icon {
    width: 26px; height: 26px;
    background: var(--green);
    display: flex; align-items: center; justify-content: center;
  }
  .contacts__icon svg { width: 15px; height: 15px; }
  .name-tab {
    position: absolute;
    right: 0; top: 62px;
    width: 250px; height: 40px;
    background: var(--green);
    color: var(--white);
    font-size: 19px; font-weight: 500;
    display: flex; align-items: center; padding-left: 26px;
  }
  .brand-mark {
    position: absolute;
    right: 40px; bottom: 38px;
    display: flex; align-items: center; gap: 10px;
    font-weight: 600; font-size: 18px; color: var(--green);
  }
  .brand-mark__dot { width: 40px; height: 40px; border-radius: 50%; background: var(--green); }

  /* Back */
  .card--back {
    top: 470px;
    background: radial-gradient(circle at 50% 38%, var(--green-light) 0%, #4cc63a 35%, var(--green) 75%);
  }
  .back-brand {
    position: absolute;
    left: 0; right: 0; top: 105px;
    display: flex; align-items: center; justify-content: center; gap: 12px;
    font-weight: 600; font-size: 24px; color: var(--white);
  }
  .back-brand__dot { width: 46px; height: 46px; border-radius: 50%; background: var(--white); }
  .review-band {
    position: absolute;
    left: 0; right: 0; bottom: 0; height: 92px;
    background: var(--green-dark);
    color: var(--white);
    text-align: center;
    padding-top: 16px;
  }
  .review-band__title { font-size: 20px; font-weight: 700; text-transform: uppercase; letter-spacing: .3px; }
  .review-band__url { font-size: 18px; font-weight: 400; margin-top: 2px; }
</style>
</head>
<body>

<section class="card card--front" aria-label="Business card front">
  <div class="side-bar side-bar--top"></div>
  <div class="side-bar side-bar--bottom"></div>

  <div class="identity">
    <h1 class="identity__name">Darren Holloway</h1>
    <p class="identity__role">Managing Director</p>
  </div>

  <ul class="contacts">
    <li class="contacts__item">
      <span class="contacts__icon">
        <svg viewBox="0 0 16 16"><path d="M4 1.5l2.2 3-1.4 1.6a8 8 0 0 0 5.1 5.1l1.6-1.4 3 2.2-1.2 2.5C7.5 14.3 1.7 8.5 1.5 2.7z" fill="#fff"/></svg>
      </span>
      0491 570 156
    </li>
    <li class="contacts__item">
      <span class="contacts__icon">
        <svg viewBox="0 0 16 16"><rect x="1.5" y="3.5" width="13" height="9" fill="none" stroke="#fff" stroke-width="1.4"/><path d="M1.5 3.5L8 9l6.5-5.5" fill="none" stroke="#fff" stroke-width="1.4"/></svg>
      </span>
      darren@clearpathwaste.com.au
    </li>
    <li class="contacts__item">
      <span class="contacts__icon">
        <svg viewBox="0 0 16 16"><circle cx="8" cy="8" r="6.3" fill="none" stroke="#fff" stroke-width="1.3"/><ellipse cx="8" cy="8" rx="2.8" ry="6.3" fill="none" stroke="#fff" stroke-width="1.1"/><path d="M1.7 8h12.6" stroke="#fff" stroke-width="1.1"/></svg>
      </span>
      clearpathwaste.com.au
    </li>
  </ul>

  <div class="name-tab">Clearpath Waste Co</div>

  <div class="brand-mark">
    <span class="brand-mark__dot"></span>
    Clearpath Waste Co
  </div>
</section>

<section class="card card--back" aria-label="Business card back">
  <div class="back-brand">
    <span class="back-brand__dot"></span>
    Clearpath Waste Co
  </div>
  <div class="review-band">
    <p class="review-band__title">How did we do?</p>
    <p class="review-band__url">clearpathwaste.com.au/review</p>
  </div>
</section>

</body>
</html>
```